Textbook cover for dental seminar

I'm looking for a fresh new design for our annual textbook. You will need to incorporate our logo, business name (LoriKSM's Dental Hygiene Academy) - the words "LoriKSM's" needs to be larger or the same size as "Dental Hygiene Academy" and colors of dentistry is purple so I like to stick with shades of purple in the design however it does not need to be all purple or only purple. The words "with hygiene career booster" will not be on next years edition so please do not add that. The book will have spiral binding so please account for that when designing. Please see our website for information LoriKSMExamPrep.com

I also want listed on the cover somewhere “The World’s First Interactive Review Book!”

Size will be 8.5" x 11"

```html
<!DOCTYPE html>
<html lang="en">
<head>
<meta charset="utf-8">
<title>LoriKSM's Dental Hygiene Academy – Textbook Cover</title>
<link rel="stylesheet" href="https://fonts.googleapis.com/css2?family=Montserrat:wght@700;800;900&display=swap">
<style>
  :root {
    --page-bg: #8c989f;
    --navy-purple: #1f0b4e;
    --magenta: #8d2a8e;
    --orange: #f28a1e;
    --white: #ffffff;
    --ribbon-purple: #8a1f8e;
    --ribbon-navy: #1f0b4e;
    --badge-black: #111111;
  }
  * { margin: 0; padding: 0; box-sizing: border-box; }
  html, body {
    width: 808px; height: 1200px; overflow: hidden;
    background: var(--page-bg);
    font-family: "Montserrat", Arial, sans-serif;
  }
  /* 8.5 x 11 in cover: 808 x 1046 px */
  .cover {
    position: absolute; left: 0; top: 77px;
    width: 808px; height: 1046px;
    background: var(--navy-purple); overflow: hidden;
  }
  .shapes { position: absolute; inset: 0; }
  .wave-decoration {
    position: absolute; left: 579px; top: 448px; width: 229px; height: 598px;
    background: linear-gradient(160deg, rgba(233,225,245,0.04), rgba(233,225,245,0.3) 50%, rgba(233,225,245,0.04));
    clip-path: polygon(45% 0, 100% 8%, 100% 100%, 62% 100%, 22% 55%);
  }
  .site-url {
    position: absolute; left: 76px; top: 521px;
    transform: translate(-50%, -50%) rotate(-90deg);
    white-space: nowrap;
    color: var(--orange); font-weight: 800; font-size: 36px;
    letter-spacing: 4px;
  }
  .ribbon {
    position: absolute; left: 548px; top: 0; width: 216px; height: 230px;
    background: var(--white);
    clip-path: polygon(0 0, 100% 0, 100% 100%, 50% 88%, 0 100%);
    text-align: center; padding-top: 34px; line-height: 1.0;
  }
  .ribbon .line { display: block; font-weight: 800; }
  .ribbon .accent { color: var(--ribbon-purple); font-size: 23px; }
  .ribbon .strong { color: var(--ribbon-navy); font-size: 31px; font-weight: 900; }
  .title {
    position: absolute; left: 139px; top: 362px;
    color: var(--white); font-weight: 900; font-size: 62px;
    line-height: 64px; text-transform: uppercase;
  }
  .academy-mark {
    position: absolute; left: 264px; top: 648px; width: 268px; height: 268px;
    border-radius: 50%; background: var(--white);
    display: flex; align-items: center; justify-content: center;
    text-align: center; color: var(--magenta);
    font-weight: 800; font-size: 27px; line-height: 1.15; padding: 34px;
  }
  .app-call {
    position: absolute; left: 136px; top: 954px;
    color: var(--white); font-weight: 800; font-size: 23px;
  }
  .store-badges { position: absolute; left: 136px; top: 988px; display: flex; gap: 6px; }
  .store-badge {
    width: 100px; height: 32px; border-radius: 5px;
    background: var(--badge-black); border: 1px solid #777;
    color: var(--white); font-weight: 700; font-size: 12px;
    display: flex; align-items: center; justify-content: center;
  }
  .tagline {
    position: absolute; right: 30px; top: 958px; width: 330px;
    text-align: right; color: var(--white);
    font-weight: 800; font-size: 19px; line-height: 1.25; text-transform: uppercase;
  }
</style>
</head>
<body>
<main class="cover">
  <svg class="shapes" width="808" height="1046" viewBox="0 0 808 1046" aria-hidden="true">
    <defs>
      <radialGradient id="blobGlow" cx="0.35" cy="0.4" r="0.7">
        <stop offset="0" stop-color="#9c3a9e" stop-opacity="0.9"/>
        <stop offset="1" stop-color="#5c1d72" stop-opacity="0"/>
      </radialGradient>
    </defs>
    <circle class="lower-blob" cx="190" cy="740" r="140" fill="url(#blobGlow)"/>
    <circle class="main-disc" cx="403" cy="508" r="300" fill="var(--magenta)"/>
    <circle class="ring" cx="234" cy="247" r="46" fill="none" stroke="var(--white)" stroke-width="4"/>
    <circle class="dot" cx="286" cy="214" r="29" fill="var(--white)"/>
  </svg>

  <div class="wave-decoration" role="img" aria-label="Flowing fine-line wave pattern"></div>

  <div class="site-url">WWW.LORIKSMEXAMPREP.COM</div>

  <div class="ribbon">
    <span class="line accent">The Nations'</span>
    <span class="line strong">#1 LIVE or</span>
    <span class="line strong">ONLINE</span>
    <span class="line accent">Board Review</span>
    <span class="line accent">Seminar!</span>
  </div>

  <h1 class="title">LoriKSM's<br>Dental<br>Hygiene<br>Academy</h1>

  <div class="academy-mark">LoriKSM's Dental Hygiene Academy</div>

  <div class="app-call">GET APP AN</div>
  <div class="store-badges">
    <div class="store-badge">Droid Market</div>
    <div class="store-badge">PocketStore</div>
  </div>

  <p class="tagline">The World’s First<br>Interactive Review Book!</p>
</main>
</body>
</html>
```